In Home Senior Care Agency Business Card Design Needed

At Silver Birch Helpers, we don't just work in the care-giving industry. We truly care.

We are dedicated to providing personable, hands-on and integrated caring services that aim to help people maintain safe and comfortable life standards within the familiar settings of their own homes.

We would like to see designs that use my logo colors obviously. The final design will be modern, yet professional and semi-minimalistic. It should communicate an well-established company that is innovative. We would also like the design to have that 'flat' design look. Ideally having the design roll over to the backend of the card. Most likely it will be printed on a Matte paper with a die cut (either 2 rounded corners -leaf cut) or all rounded.

Target Market(s)

Baby boomer generation. 45 years and older.

Industry/Entity Type

Business

Contact Information for Business Card

Text for Front:
Slogan somewhere "Your Home. Our Helping Hands.”

Darren Whitlow
President

Cell: 917.284.6051
Phone: 917.512.7368
E: Darren@silverbirchhelpers.com
W: www.SilverBirchHelpers.com

Back:
-Meal Preparation
-Transportation
-Light Housekeeping
-Bathing Assistance
-Companionship

Font styles to use
Serif
Sans Serif

Requirements
Must have
• Flat, modern, professional design. Not too many colors. Match my colors in logo. Design of card must reflect from the front onto the back. Evenly spaced font.
Nice to have
• Try to work off current logo scheme, but logo may need to be redesigned.
Should not have
• Not too many colors.

```html
<!DOCTYPE html>
<html lang="en">
<head>
<meta charset="utf-8">
<title>Silver Birch Helpers – Business Cards</title>
<link rel="stylesheet" href="https://fonts.googleapis.com/css2?family=Open+Sans:wght@400;600;700&display=swap">
<style>
  :root {
    --page: #ffffff;
    --card: #262626;
    --card-edge: #1c1c1c;
    --ink-white: #f2f2f2;
    --ink-faint: #575757;
    --chevron: #9a9a9a;
    --brand-green: #1d6b3a;
    --brand-gold: #e3a534;
    --font-text: "Open Sans", Arial, sans-serif;
  }
  * { box-sizing: border-box; margin: 0; padding: 0; }
  html, body { width: 1200px; height: 900px; overflow: hidden; background: var(--page); }
  .canvas { position: relative; width: 1200px; height: 900px; font-family: var(--font-text); }

  .card {
    position: absolute;
    width: 560px;
    height: 320px;
    background: var(--card);
    border-radius: 6px;
    box-shadow: 0 3px 0 var(--card-edge), 0 10px 24px rgba(0,0,0,.18);
    overflow: hidden;
  }
  .card--back { left: 110px; top: 100px; }
  .card--front { left: 530px; top: 470px; }

  /* Back */
  .back-wordmark {
    position: absolute;
    left: 0; right: 0; top: 72px;
    text-align: center;
    font-size: 44px;
    font-weight: 600;
    line-height: 1.05;
    color: var(--ink-faint);
  }
  .services { list-style: none; position: absolute; }
  .services--one { left: 34px; bottom: 34px; }
  .services--two { left: 220px; bottom: 56px; }
  .services--three { left: 384px; bottom: 78px; }
  .services__item {
    display: flex; align-items: center; gap: 9px;
    font-size: 15px;
    line-height: 22px;
    color: var(--ink-white);
    white-space: nowrap;
  }
  .services__chevron { width: 6px; height: 10px; flex: none; }

  /* Front */
  .person { position: absolute; left: 54px; top: 70px; }
  .person__name { font-size: 19px; font-weight: 700; letter-spacing: .5px; color: var(--ink-white); text-transform: uppercase; white-space: nowrap; }
  .person__title { font-size: 14px; color: var(--brand-green); margin-top: 2px; }

  .front-wordmark {
    position: absolute;
    left: 300px; top: 48px;
    display: flex; align-items: center; gap: 10px;
    font-size: 24px;
    font-weight: 600;
    line-height: 1.05;
    color: var(--brand-gold);
  }
  .front-wordmark__dot { width: 14px; height: 14px; border-radius: 50%; background: var(--brand-gold); flex: none; }

  .slogan {
    position: absolute;
    right: 10px; top: 0; bottom: 0;
    width: 26px;
    writing-mode: vertical-rl;
    transform: rotate(180deg);
    text-align: center;
    font-size: 14px;
    letter-spacing: .4px;
    color: var(--brand-green);
    white-space: nowrap;
  }

  .contact { position: absolute; left: 54px; bottom: 38px; list-style: none; }
  .contact__item {
    display: flex; align-items: center; gap: 12px;
    font-size: 17px;
    line-height: 24px;
    color: var(--ink-white);
    white-space: nowrap;
  }
  .contact__icon { width: 11px; height: 11px; flex: none; }
</style>
</head>
<body>
<main class="canvas">

  <section class="card card--back" aria-label="Card back">
    <div class="back-wordmark">Silver Birch<br>Helpers</div>
    <ul class="services services--one">
      <li class="services__item"><svg class="services__chevron" viewBox="0 0 6 10"><path d="M1 1l4 4-4 4" fill="none" stroke="var(--chevron)" stroke-width="1.2"/></svg>Meal Preparation</li>
      <li class="services__item"><svg class="services__chevron" viewBox="0 0 6 10"><path d="M1 1l4 4-4 4" fill="none" stroke="var(--chevron)" stroke-width="1.2"/></svg>Bathing Assistance</li>
    </ul>
    <ul class="services services--two">
      <li class="services__item"><svg class="services__chevron" viewBox="0 0 6 10"><path d="M1 1l4 4-4 4" fill="none" stroke="var(--chevron)" stroke-width="1.2"/></svg>Transportation</li>
      <li class="services__item"><svg class="services__chevron" viewBox="0 0 6 10"><path d="M1 1l4 4-4 4" fill="none" stroke="var(--chevron)" stroke-width="1.2"/></svg>Companionship</li>
    </ul>
    <ul class="services services--three">
      <li class="services__item"><svg class="services__chevron" viewBox="0 0 6 10"><path d="M1 1l4 4-4 4" fill="none" stroke="var(--chevron)" stroke-width="1.2"/></svg>Light Housekeeping</li>
    </ul>
  </section>

  <section class="card card--front" aria-label="Card front">
    <div class="person">
      <p class="person__name">Darren Whitlow</p>
      <p class="person__title">President</p>
    </div>

    <div class="front-wordmark"><span class="front-wordmark__dot"></span><span>Silver Birch<br>Helpers</span></div>

    <p class="slogan">Your Home. Our Helping Hands.</p>

    <ul class="contact">
      <li class="contact__item">
        <svg class="contact__icon" viewBox="0 0 11 11"><rect x="3" y="0.5" width="5" height="10" rx="1" fill="none" stroke="var(--brand-green)" stroke-width="1.2"/></svg>917.284.6051
      </li>
      <li class="contact__item">
        <svg class="contact__icon" viewBox="0 0 11 11"><path d="M1 4c0-2 9-2 9 0v1H7.5V4h-4v1H1z M2 6h7l1 4H1z" fill="var(--brand-green)"/></svg>917.512.7368
      </li>
      <li class="contact__item">
        <svg class="contact__icon" viewBox="0 0 11 11"><rect x="0.5" y="2" width="10" height="7" fill="var(--brand-green)"/><path d="M0.5 2l5 4 5-4" fill="none" stroke="var(--card)" stroke-width="1"/></svg>Darren@silverbirchhelpers.com
      </li>
      <li class="contact__item">
        <svg class="contact__icon" viewBox="0 0 11 11"><path d="M4.5 6.5l2-2 M3.5 5l-1.5 1.5a2 2 0 0 0 2.8 2.8L6.3 7.8 M7.5 6l1.5-1.5a2 2 0 0 0-2.8-2.8L4.7 3.2" fill="none" stroke="var(--brand-green)" stroke-width="1.3"/></svg>www.SilverBirchHelpers.com
      </li>
    </ul>
  </section>

</main>
</body>
</html>
```